Brinewardsea.com Website design needed!!

We are looking for a website layout to match the attached logo. We specialize in Dive Charters and currently are located in the Virgin Islands off of Marrowick Isle. Please create a design that is compatible with Bootstrap and have the grid in mind. WE are looking for creative and extremely professional layout design.

Target Market(s)

Scuba Diving, Divers looking for a diving charter in the Virgin Islands.

Number of Pages Required

3 page

Font styles to use
Serif

Requirements
Must have
• Must be Bootstrap friendly.
• Must work with the logo we provided. Colors etc.

```html
<!DOCTYPE html>
<html lang="en">
<head>
<meta charset="utf-8">
<title>Brinewardsea Marrowick Isle – Dive Charters</title>
<link href="https://fonts.googleapis.com/css2?family=Cinzel:wght@400;700&family=Arimo:ital,wght@0,400;0,700;1,400&family=Oswald:wght@400;500&family=Kaushan+Script&display=swap" rel="stylesheet">
<style>
:root{
  --cream:#f7f1e3;
  --cream-dark:#efe6d3;
  --red:#e31e24;
  --red-soft:#e4554a;
  --teal:#4dbfa0;
  --teal-light:#55d0a8;
  --orange:#e8821e;
  --ink:#333333;
  --muted:#777066;
  --blue-deep:#0a5fae;
  --white:#ffffff;
  --gold:#b59a5c;
}
*{box-sizing:border-box;margin:0;padding:0}
html,body{width:1200px;height:2723px;overflow:hidden}
body{position:relative;background:var(--white);font-family:"Arimo",Arial,sans-serif;color:var(--ink)}
.abs{position:absolute}

/* top bar + header */
.top-bar{left:0;top:0;width:1200px;height:37px;background:var(--cream);border-bottom:1px solid var(--cream-dark);font-size:14px;line-height:37px;color:#444}
.top-bar .call{left:70px}
.top-bar .mail{left:440px}
.top-bar a{color:var(--orange);text-decoration:none}
.top-social{top:5px;display:flex;gap:6px;left:980px}
.dot-icon{width:26px;height:26px;border:1.5px solid #555;border-radius:50%}
.search-btn{left:1080px;top:0;width:50px;height:37px;border-left:1px solid var(--cream-dark);border-right:1px solid var(--cream-dark)}
.site-header{left:0;top:37px;width:1200px;height:170px;background:var(--cream)}
.brand{left:86px;top:92px;display:flex;align-items:center;gap:12px}
.brand-mark{width:30px;height:30px;border-radius:50%;background:var(--blue-deep)}
.brand-name{font-family:"Cinzel",serif;font-weight:700;font-size:34px;color:var(--red);line-height:1}
.brand-sub{left:112px;top:135px;font-family:"Cinzel",serif;font-weight:700;font-size:15px;letter-spacing:3px;color:var(--blue-deep)}
.main-nav a{position:absolute;top:61px;font-family:"Arimo",sans-serif;font-weight:700;font-size:15px;color:#8a8272;text-decoration:none;letter-spacing:.3px}

/* hero */
.hero-photo{left:0;top:160px;width:1200px;height:640px;background:linear-gradient(160deg,#0d4f7e 0%,#1c7fae 38%,#2aa0c0 62%,#3a7d8e 82%,#6b6a58 100%)}
.hero-wave-top{left:0;top:150px}
.hero-title{left:76px;top:440px;font-family:"Kaushan Script",cursive;font-size:46px;color:var(--white)}
.btn-check{left:192px;top:613px;width:367px;height:62px;border:3px solid var(--white);border-radius:31px;background:var(--red);color:var(--white);font-family:"Oswald",sans-serif;font-weight:500;font-size:31px;line-height:56px;text-align:center}
.slider-arrows{left:73px;top:712px;display:flex;gap:4px}
.slider-arrows span{width:26px;height:26px;border:1.5px solid rgba(255,255,255,.7);display:block}
.slider-arrows span.active{border-color:var(--white)}

.search-panel{left:697px;top:428px;width:412px;height:318px;background:rgba(22,26,30,.88);border-radius:20px 20px 0 0}
.search-head{height:84px;background:var(--red);border-radius:20px 20px 0 0;padding:16px 0 0 28px;font-family:"Cinzel",serif;font-size:25px;line-height:27px;color:var(--white)}
.radio-row{position:absolute;left:28px;display:flex;align-items:center;gap:10px;font-size:13px;color:var(--white)}
.radio-row i{width:14px;height:14px;border-radius:50%;background:var(--white);display:block}
.radio-row i.on{box-shadow:inset 0 0 0 4px var(--white);background:#777}
.field{position:absolute;top:170px;width:173px;height:40px;background:var(--white);border-radius:3px;font-size:13px;color:#888;line-height:40px;padding-left:12px}
.btn-find{position:absolute;left:29px;top:230px;width:356px;height:44px;background:var(--orange);border-radius:3px;color:var(--white);font-family:"Oswald",sans-serif;font-size:22px;line-height:44px;text-align:center;letter-spacing:.5px}

/* welcome */
.welcome-band{left:0;top:700px}
.welcome{left:0;top:852px;width:1200px;text-align:center;color:var(--white)}
.welcome .kicker{font-family:"Cinzel",serif;font-size:25px;letter-spacing:4px}
.welcome h1{font-family:"Cinzel",serif;font-weight:400;font-size:34px;letter-spacing:2px;margin-top:-2px}
.welcome p{width:990px;margin:20px auto 0;font-size:13px;line-height:24px}
.more-link{left:568px;top:1062px;display:flex;align-items:center;gap:8px;font-size:12px;font-weight:700;color:var(--white)}
.ring{width:20px;height:20px;border:2px solid currentColor;border-radius:50%;display:flex;align-items:center;justify-content:center}

/* news + video */
.news-panel{left:74px;top:1222px;width:540px;height:345px;background:var(--cream-dark)}
.news-tabs{height:58px;background:var(--red-soft);position:relative}
.tab{position:absolute;top:20px;height:38px;line-height:38px;font-size:16px;text-align:center}
.tab-news{left:14px;width:84px;background:var(--cream-dark);color:#333}
.tab-events{left:98px;width:81px;background:#ee8b80;color:var(--white)}
.news-item{position:absolute;left:18px;display:flex;gap:16px}
.thumb{width:94px;height:94px;background:linear-gradient(135deg,#0d5fa6,#2a9fd6 60%,#f0c040)}
.thumb.boat{background:linear-gradient(135deg,#8ec7e8,#ffffff 55%,#d44a3a)}
.news-item h3{font-size:16px;font-weight:400;color:#333;margin-top:10px}
.news-item .date{font-size:11px;color:#555;margin-top:4px}
.news-item p{font-size:12.5px;line-height:20px;color:#555;margin-top:8px;width:400px}
.news-foot{position:absolute;left:0;bottom:0;width:540px;height:39px;border-top:1px solid #ddd2bc;display:flex;align-items:center;gap:10px;padding-left:26px;font-size:12px;color:#444}
.news-foot .ring{color:var(--red)}
.video-panel{left:614px;top:1222px;width:511px;height:345px}
.video-frame{width:511px;height:306px;background:radial-gradient(circle at 62% 30%,#6fd0f2 0%,#1f86c6 30%,#0c4c8a 70%,#06305d 100%)}
.video-foot{width:511px;height:39px;background:var(--teal-light);display:flex;align-items:center;gap:10px;padding-left:14px;font-size:12px;color:var(--white)}
.play{left:213px;top:113px}

/* feedback */
.feedback{left:0;top:1612px;width:1200px;height:420px;background:var(--cream)}
.feedback h2{position:absolute;top:46px;width:1200px;text-align:center;font-family:"Cinzel",serif;font-weight:400;font-size:36px;color:var(--teal)}
.feedback .sub{position:absolute;top:92px;width:1200px;text-align:center;font-size:12px;color:var(--gold)}
.quote-mark{position:absolute;top:128px;font-family:"Cinzel",serif;font-size:60px;color:var(--gold)}
.feedback blockquote{position:absolute;left:262px;top:140px;width:676px;text-align:center;font-style:italic;font-size:13px;line-height:24px;color:#555}
.author{position:absolute;top:283px;width:1200px;text-align:center;font-size:15px;font-weight:700;color:var(--red)}
.author-role{position:absolute;top:306px;width:1200px;text-align:center;font-size:11px;color:var(--muted)}
.dots{position:absolute;top:350px;left:564px;display:flex;gap:5px}
.dots i{width:9px;height:9px;border-radius:50%;background:#cfc4a8;display:block}
.dots i.on{width:12px;height:12px;margin-top:-1.5px;background:var(--red)}

/* footer */
.site-footer{left:0;top:1990px;width:1200px;height:733px;background:linear-gradient(180deg,#1b9be0 0%,#138ad4 45%,#0b6fc0 100%)}
.footer-wave{left:0;top:1980px}
.footer-photo{left:630px;top:2280px;width:470px;height:420px;background:radial-gradient(ellipse at 50% 45%,rgba(10,50,110,.55) 0%,rgba(10,60,130,.25) 45%,rgba(21,150,220,0) 75%)}
.footer-brand{left:656px;top:2180px;width:400px;text-align:center}
.footer-brand .brand-name{font-size:46px}
.footer-brand .brand-sub{position:static;display:block;margin-top:8px;font-size:19px;color:var(--white);letter-spacing:4px}
.footer-title{left:76px;top:2148px;font-family:"Cinzel",serif;font-weight:400;font-size:58px;line-height:60px;color:var(--white);letter-spacing:2px}
.footer-rule{left:76px;top:2298px;width:38px;height:2px;background:rgba(255,255,255,.4)}
.f-col{font-size:13px;line-height:24px;color:var(--white)}
.f-col h4{font-size:15px;font-weight:700;margin-bottom:6px}
.f-social{left:476px;top:2344px;display:flex;gap:6px}
.f-social .dot-icon{border-color:var(--white);width:30px;height:30px}
.newsletter-label{left:76px;top:2458px;font-size:15px;font-weight:700;color:var(--white)}
.newsletter-input{left:76px;top:2512px;width:432px;height:34px;border-bottom:1px solid rgba(255,255,255,.7);font-size:21px;color:var(--white)}
.btn-subscribe{left:76px;top:2552px;width:189px;height:54px;border:1.5px solid var(--white);color:var(--white);font-size:22px;font-weight:700;text-align:center;line-height:51px}
.footer-nav{left:79px;top:2632px;display:flex}
.footer-nav a{color:var(--white);font-size:12px;text-decoration:none}
.copyright{left:76px;top:2678px;font-size:13px;color:var(--white)}
</style>
</head>
<body>

<div class="abs top-bar">
  <span class="abs call">I case of any Questions, Please Call: <a href="#">(555)-013-2846</a></span>
  <span class="abs mail">Email: <a href="#">info@brinewardsea.com</a></span>
  <div class="abs top-social"><span class="dot-icon"></span><span class="dot-icon"></span><span class="dot-icon"></span></div>
  <div class="abs search-btn">
    <svg width="50" height="37" viewBox="0 0 50 37"><circle cx="23" cy="16" r="7" fill="none" stroke="#333" stroke-width="2.4"/><line x1="28" y1="21" x2="33" y2="26" stroke="#333" stroke-width="2.8" stroke-linecap="round"/></svg>
  </div>
</div>

<header class="abs site-header">
  <nav class="main-nav">
    <a href="#" style="left:457px">BRINEWARDSEA</a>
    <a href="#" style="left:623px">ABOUT US</a>
    <a href="#" style="left:755px">CONTACT</a>
    <a href="#" style="left:884px">LEARN MORE</a>
    <a href="#" style="left:1038px">SCHEDULE</a>
  </nav>
</header>

<div class="abs hero-photo" role="img" aria-label="Scuba diver swimming over a colourful coral reef with tropical fish"></div>
<svg class="abs hero-wave-top" width="1200" height="60" viewBox="0 0 1200 60">
  <path d="M0 0 H1200 V8 C1000 10 800 50 550 48 C350 46 150 24 0 20 Z" fill="var(--cream)"/>
  <path d="M0 20 C150 24 350 46 550 48 C800 50 1000 10 1200 8 V18 C1000 22 800 60 550 58 C350 56 150 34 0 30 Z" fill="var(--red)"/>
</svg>

<div class="abs brand"><span class="brand-mark"></span><span class="brand-name">Brinewardsea</span></div>
<div class="abs brand-sub">MARROWICK ISLE</div>

<div class="abs hero-title">Lorem ipsum dolor sit amet</div>
<div class="abs btn-check">CHECK AVAILABILITY</div>
<div class="abs slider-arrows">
  <span><svg width="23" height="23" viewBox="0 0 23 23"><path d="M14 6 L8 11.5 L14 17 Z" fill="rgba(255,255,255,.7)"/></svg></span>
  <span class="active"><svg width="23" height="23" viewBox="0 0 23 23"><path d="M9 6 L15 11.5 L9 17 Z" fill="#fff"/></svg></span>
</div>

<svg class="abs welcome-band" width="1200" height="470" viewBox="0 0 1200 470">
  <path d="M0 70 C250 50 500 35 720 45 C920 55 1080 30 1200 20 V420 C1000 400 800 450 600 450 C380 450 180 405 0 400 Z" fill="var(--teal)"/>
</svg>

<div class="abs search-panel">
  <div class="search-head">SEARCH FOR YOUR<br>DREAM CHARTER TODAY!</div>
  <div class="radio-row" style="top:108px"><i class="on"></i>I have approximate dates</div>
  <div class="radio-row" style="top:135px"><i></i>I'm flexible</div>
  <div class="field" style="left:29px">First Name</div>
  <div class="field" style="left:212px">Email</div>
  <div class="btn-find">FIND CHARTERS</div>
</div>

<section class="abs welcome">
  <div class="kicker">WELCOME TO</div>
  <h1>BRINEWARDSEA CHARTERS AND SCUBA</h1>
  <p>Lorem ipsum dolor sit amet, consectetur adipiscing elit. Fusce semper vitae leo sit amet vehicula. Sed viverra, justo ac consectetur hendrerit, lacus elit tempor urna, gravida mattis lacus ex sed sem. Nam consectetur, arcu in iaculis dapibus, urna felis congue elit, in consectetur nisi massa sed metus. Nullam a tortor ut mauris auctor interdum id vel neque. In commodo diam at faucibus dictum. Nulla condimentum elit a odio consectetur, vel eleifend libero sagittis. Praesent sed erat a ante laoreet dapibus et ultrices sem. Vivamus elit lectus, ullamcorper et vestibulum eget</p>
</section>
<div class="abs more-link"><span class="ring"><svg width="10" height="10" viewBox="0 0 10 10"><path d="M3.5 1.5 L7 5 L3.5 8.5" fill="none" stroke="#fff" stroke-width="1.8"/></svg></span>MORE</div>

<section class="abs news-panel">
  <div class="news-tabs"><div class="tab tab-news">News</div><div class="tab tab-events">Events</div></div>
  <article class="news-item" style="top:78px">
    <div class="thumb" role="img" aria-label="Two divers underwater"></div>
    <div><h3>This is a test Title</h3><div class="date">18 JAN 2016</div><p>Lorem ipsum dolor sit amet, consectetur adipiscing elit. Fusce semper vitae leo sit amet vehicula.</p></div>
  </article>
  <article class="news-item" style="top:192px">
    <div class="thumb boat" role="img" aria-label="Guests aboard a dive charter boat"></div>
    <div><h3>This is a test Title</h3><div class="date">18 JAN 2016</div><p>Lorem ipsum dolor sit amet, consectetur adipiscing elit. Fusce semper vitae leo sit amet vehicula.</p></div>
  </article>
  <div class="news-foot"><span class="ring"><svg width="10" height="10" viewBox="0 0 10 10"><path d="M3.5 1.5 L7 5 L3.5 8.5" fill="none" stroke="#e31e24" stroke-width="1.8"/></svg></span>VIEW MORE NEWS</div>
</section>

<section class="abs video-panel">
  <div class="video-frame" role="img" aria-label="Video still of a diver silhouetted against sunlit blue water"></div>
  <svg class="abs play" width="86" height="86" viewBox="0 0 86 86"><circle cx="43" cy="43" r="38" fill="rgba(255,255,255,.15)" stroke="#fff" stroke-width="5"/><path d="M34 25 L62 43 L34 61 Z" fill="#fff"/></svg>
  <div class="video-foot"><span class="ring"><svg width="10" height="10" viewBox="0 0 10 10"><path d="M3.5 1.5 L7 5 L3.5 8.5" fill="none" stroke="#fff" stroke-width="1.8"/></svg></span>VIEW MORE VIDEOS</div>
</section>

<section class="abs feedback">
  <h2>GUEST FEEDBACK</h2>
  <div class="sub">WHAT OUR GUESTS THINK OF US</div>
  <span class="quote-mark" style="left:214px">“</span>
  <span class="quote-mark" style="left:955px">”</span>
  <blockquote>Lorem ipsum dolor sit amet, consectetur adipiscing elit. Fusce semper vitae leo sit amet vehicula. Sed viverra, justo ac consectetur hendrerit, lacus elit tempor urna, gravida mattis lacus ex sed sem. Nam consectetur, arcu in iaculis dapibus, urna felis congue elit, in consectetur nisi massa sed metus. Nullam a tortor ut mauris auctor interdum id vel neque. In commodo diam at faucibus dictum. Nulla condimentum elit a odio consectetur, vel eleifend libero sagittis.</blockquote>
  <div class="author">JOHN DOE</div>
  <div class="author-role">Lorem ipsum dolor</div>
  <div class="dots"><i class="on"></i><i></i><i></i><i></i><i></i><i></i></div>
</section>

<footer class="abs site-footer"></footer>
<svg class="abs footer-wave" width="1200" height="90" viewBox="0 0 1200 90">
  <path d="M0 0 H1200 V50 C1000 55 850 70 650 80 C420 90 200 40 0 10 Z" fill="var(--cream)"/>
  <path d="M0 10 C200 40 420 90 650 80 C850 70 1000 55 1200 50 V64 C1000 68 850 84 650 92 C420 100 200 54 0 26 Z" fill="var(--red)"/>
</svg>
<div class="abs footer-photo" role="img" aria-label="Scuba diver descending in deep blue water"></div>
<div class="abs footer-brand"><span class="brand-name">Brinewardsea</span><span class="brand-sub">MARROWICK ISLE</span></div>

<h2 class="abs footer-title">GET IN TOUCH<br>WITH US</h2>
<div class="abs footer-rule"></div>
<div class="abs f-col" style="left:76px;top:2340px"><h4>Contact Us</h4>info@yourdomain.com<br>Cell: (555)-013-2846</div>
<div class="abs f-col" style="left:300px;top:2340px"><h4>Visit Us</h4>Your Company LTD.<br>Street Name, 000000<br>City Name</div>
<div class="abs f-social"><span class="dot-icon"></span><span class="dot-icon"></span><span class="dot-icon"></span></div>
<div class="abs newsletter-label">Newsletter</div>
<div class="abs newsletter-input">Enter your email address</div>
<div class="abs btn-subscribe">Subscribe</div>
<nav class="abs footer-nav">
  <a href="#" style="width:145px">BRINEWARDSEA</a>
  <a href="#" style="width:115px">ABOUT US</a>
  <a href="#" style="width:113px">CONTACT</a>
  <a href="#" style="width:138px">LEARN MORE</a>
  <a href="#">SCHEDULE</a>
</nav>
<div class="abs copyright">© 2016 BRINEWARDSEA MARROWICK ISLE. ALL RIGHTS RESERVED</div>

</body>
</html>
```